Migration and redesign of existing website to WordPress using DIVI 3

I. TASK OBJECTIVE:
- Redesign our existing website www.calderwynhealth.com.au with a fresh new look and migrate to new Wordpress site based on DIVI3 theme. The site will contain the same basic functionality as the existing site (with some small changes).

II. STYLE/ DESIGN ASPECT:
As an example of a site that I like the look of, see https://tanglorix.com/. I like the use of shadows, and this would go well with the little animations you can do with Divi (e.g. when hovering over pics).

1. What I am looking for is a design which has lots of white space, is modern and friendly looking (but still not too cute or frivolous, as we are a medical practice)
2. DESIGN that is NOT TOO rectangular or blocky.
3. Please take into consideration our Users are Older market, so any icons or navigation features need to be very easy to understand and not too small.
4. Must be easy to navigate
5. We are are happy to go with a new colour scheme, and are working on some ideas for this, but happy to take suggestions.

III. SPECIFICATIONS:
1. 5+ Pages (should flow like the current site)
2. Using Wordpress Divi 3 theme.
3. I'd like every page to have a "book now" button and a contact form in a sidebar so that users can click the button or fill in the contact form without scrolling at all. EXCEPT ON THE HOME PAGE, where there should still be a book now button (maybe on the top right in the header of all pages?), and maybe a contact us button which scrolls down to the contact area at the bottom of the HOME page. I don't think a side bar is necessarily required on the home page, but if you think it makes sense from a design perspective please let me know.
4. AT THE BOTTOM OF THE PAGE, just above the FOOTER, I'd like a row of trust logos for various organisations that we are affiliated with. (A list of this company will be provided later but you could temporarily use placeholders)

Once we have a structure in place, we can migrate most of the content. Please let me know if I'm not being clear or you need further information.

Target Market(s)

Podiatry Customers and Referrors

Industry/Entity Type

Health Care

Coding

Coded - Design and coding required

Number of Pages Required

5+ page

Colors

Designer to choose colors to be used in the design.

Requirements
Must have
• Simple to navigate.
• Contact/booking details on most if not all pages - please see specification above
• Section for Trusted Affiliates above the footer
• Wordpress using Divi3 Theme
Nice to have
• Not too busy with the design. Plenty of white space or light background.
Should not have
• Should not be complicated to navigate.
• TOO rectangular or blocky designs

```html
<!DOCTYPE html>
<html lang="en">
<head>
<meta charset="utf-8">
<title>Calderwyn Health – Podiatry</title>
<link href="https://fonts.googleapis.com/css2?family=Raleway:wght@300;400;600;700;800&family=Open+Sans:wght@400;600&display=swap" rel="stylesheet">
<style>
:root{
  --teal:#2bb5cf;
  --teal-dark:#1f9fb8;
  --ink:#262a2e;
  --body:#6d7379;
  --muted:#9aa0a6;
  --line:#e3e6e9;
  --soft:#f3f4f5;
  --paper:#ffffff;
  --night:#2b2d30;
  --night-2:#222427;
  --shadow:0 12px 32px rgba(20,40,60,.10);
}
*{box-sizing:border-box;margin:0;padding:0}
html,body{width:1200px;height:5042px;overflow:hidden;background:var(--paper)}
body{font-family:"Open Sans",Arial,sans-serif;color:var(--body);font-size:15px;line-height:1.7;position:relative}
h1,h2,h3,h4{font-family:"Raleway",Arial,sans-serif;color:var(--ink)}
.section{position:absolute;left:0;width:1200px;overflow:hidden}
.abs{position:absolute}
.teal{color:var(--teal)}
.btn{display:inline-flex;align-items:center;gap:12px;font-family:"Raleway",sans-serif;font-weight:700;font-size:13px;letter-spacing:.5px;text-transform:uppercase;border-radius:30px}
.btn-solid{background:var(--teal);color:#fff;padding:10px 28px;box-shadow:0 6px 16px rgba(43,181,207,.35)}
.btn-line{border:2px solid var(--teal);color:var(--teal);padding:9px 24px}
.arrow{display:inline-block;width:34px;height:12px}

/* hero */
.hero{top:0;height:605px;background:linear-gradient(90deg,#eceae7 0%,#f4f3f1 45%,#f7f7f6 100%);border-radius:0 0 0 120px}
.hero-photo{left:0;top:0;width:640px;height:605px;background:radial-gradient(ellipse at 35% 40%,#d9b9a4 0%,#e8dcd3 35%,#efebe8 70%,rgba(239,235,232,0) 100%)}
.brand{left:70px;top:22px;display:flex;align-items:center;gap:10px;font-family:"Raleway",sans-serif;font-weight:700;font-size:18px;color:var(--teal-dark)}
.brand i{width:30px;height:30px;border-radius:50%;background:var(--teal-dark);display:block}
.topbar{right:60px;top:14px;display:flex;gap:22px;font-size:12px;color:var(--ink)}
.topbar span{display:flex;align-items:center;gap:6px}
.topbar svg{width:13px;height:13px}
.nav{right:60px;top:46px;display:flex;gap:24px;font-family:"Raleway",sans-serif;font-weight:600;font-size:13px;color:var(--ink)}
.nav svg{width:13px;height:13px;margin-top:3px}
.hero-title{right:60px;top:185px;text-align:right}
.hero-title .l1{font-family:"Raleway",sans-serif;font-size:30px;font-weight:400;color:var(--ink)}
.hero-title .l2{font-family:"Raleway",sans-serif;font-size:40px;font-weight:800;color:var(--ink);letter-spacing:1px;line-height:1.1}
.hero-text{right:60px;top:300px;width:510px;text-align:right;font-size:14px}
.hero-cta{right:60px;top:440px;display:flex;align-items:center;gap:16px}

/* pain */
.pain{top:605px;height:690px}
.pain-title{left:95px;top:110px;background:#fff;padding:0 12px 6px 0}
.pain-title .l1{font-family:"Raleway",sans-serif;font-size:30px;color:var(--ink)}
.pain-title .l2{font-family:"Raleway",sans-serif;font-size:36px;font-weight:800;color:var(--ink);line-height:1.1}
.pain-box{left:168px;top:85px;width:450px;height:390px;border:4px solid var(--teal);border-radius:0 40px 0 40px}
.pain-text{left:210px;top:205px;width:390px;font-size:14px;line-height:1.85}
.readmore{left:210px;top:490px;color:var(--teal);font-size:13px;display:flex;gap:10px;align-items:center}
.pain-photo{left:640px;top:110px;width:420px;height:500px;background:radial-gradient(ellipse at 50% 45%,#c7926f 0%,#d8b9a3 40%,#eef0f1 70%,rgba(255,255,255,0) 88%)}

/* practice */
.practice{top:1295px;height:655px;background:var(--soft);border-radius:80px 0 80px 0}
.sec-head{left:0;width:100%;text-align:center}
.sec-head h2{font-size:26px;font-weight:800;letter-spacing:1px}
.sec-head p{font-size:12px;letter-spacing:2px;text-transform:uppercase;color:var(--muted)}
.practice-card{left:70px;top:165px;width:1056px;height:420px;background:#fff;box-shadow:var(--shadow);border-radius:18px;overflow:hidden}
.practice-photo{left:0;top:0;width:380px;height:420px;background:linear-gradient(160deg,#6f8a47,#4f6b31 45%,#2f3b24)}
.practice-photo span{position:absolute;left:60px;bottom:16px;color:#fff;font-family:"Raleway",sans-serif;font-weight:700;font-size:12px;letter-spacing:1px}
.tabs{left:410px;top:22px;display:flex;border-bottom:1px solid var(--line);width:620px}
.tabs div{font-family:"Raleway",sans-serif;font-size:13px;color:var(--ink);padding:6px 18px 10px}
.tabs .on{color:var(--teal);border-bottom:3px solid var(--teal)}
.practice-text{left:410px;top:85px;width:620px;font-size:12.5px;line-height:1.8}
.cond{left:410px;top:290px;width:620px;display:grid;grid-template-columns:repeat(3,1fr);row-gap:4px;column-gap:20px;font-size:12.5px;color:var(--ink)}
.cond span::before{content:"";display:inline-block;width:5px;height:5px;background:var(--teal);border-radius:50%;margin-right:8px;vertical-align:middle}
.cond .more{color:var(--teal)}
.cond .more::before{display:none}

/* walks */
.walks{top:1950px;height:730px}
.walks-title{left:75px;top:70px}
.walks-title .l1{font-family:"Raleway",sans-serif;font-size:28px;color:var(--ink)}
.walks-title .l2{font-family:"Raleway",sans-serif;font-size:34px;font-weight:800;color:var(--teal);letter-spacing:1px;line-height:1.15}
.walks-text{left:75px;top:175px;width:560px;font-size:13px}
.band{left:0;top:300px;width:1050px;height:305px;background:var(--teal);border-radius:0 150px 150px 0}
.band-item{left:75px;color:#fff;font-family:"Raleway",sans-serif;font-weight:700;font-size:17px;display:flex;align-items:center;gap:14px}
.band-item svg{width:18px;height:18px}
.band-text{left:107px;top:362px;width:560px;color:#eafaff;font-size:12.5px;line-height:1.75}
.doctor{left:735px;top:40px;width:340px;height:640px;background:linear-gradient(180deg,#e6dbd2 0%,#f4f3f2 35%,#e9eef1 70%,#f8f9fa 100%);border-radius:170px 170px 30px 30px}
.walks-cta{left:75px;top:630px;display:flex;gap:16px;align-items:center}

/* team */
.team{top:2680px;height:690px}
.team-title{left:0;top:20px;width:1200px;text-align:center}
.team-title .l1{font-family:"Raleway",sans-serif;font-size:30px;color:var(--ink)}
.team-title .l2{font-family:"Raleway",sans-serif;font-size:36px;font-weight:800;color:var(--teal);line-height:1.1}
.team-text{left:310px;top:125px;width:580px;text-align:center;font-size:13.5px}
.team-grid{left:0;top:0;width:1200px;height:690px}

/* offer & cases */
.offer{top:3370px;height:745px}
.offer-title{left:75px;top:40px}
.offer-title .l1{font-family:"Raleway",sans-serif;font-size:26px;color:var(--ink)}
.offer-title .l2{font-family:"Raleway",sans-serif;font-size:30px;font-weight:800;color:var(--teal);line-height:1.1}
.offer-title .by{font-size:12px;color:var(--ink)}
.book{left:75px;top:200px;width:320px;height:450px;background:#1f5f8f;box-shadow:8px 12px 24px rgba(0,0,0,.2);border-radius:4px 14px 14px 4px}
.book h4{position:absolute;left:22px;top:24px;color:#fff;font-size:24px;font-weight:700}
.book p{position:absolute;left:22px;top:62px;color:#dbe9f3;font-size:11px;line-height:1.6}
.book .pic{position:absolute;left:22px;top:200px;width:276px;height:220px;border-radius:10px;background:linear-gradient(140deg,#3f8a9a,#2a5d6f 50%,#1d3c52)}
.book-caption{left:75px;top:668px;width:360px;font-size:12.5px;line-height:1.7}
.divider{left:548px;top:20px;width:1px;height:640px;background:var(--line)}
.cases-title{left:612px;top:40px}
.cases-title .l1{font-family:"Raleway",sans-serif;font-size:26px;color:var(--ink)}
.cases-title .l2{font-family:"Raleway",sans-serif;font-size:30px;font-weight:800;color:var(--teal);line-height:1.1}
.cases{left:612px;top:160px;width:520px}
.case{display:flex;justify-content:space-between;align-items:center;height:58px;border-bottom:1px solid var(--line);font-family:"Raleway",sans-serif;font-size:15px;color:var(--ink);padding:0 4px}
.case svg{width:22px;height:22px}

/* cta */
.strip{top:4115px;height:65px;background:var(--night);color:#fff;text-align:center;line-height:65px;font-family:"Raleway",sans-serif;font-size:17px}
.cta{top:4180px;height:365px;background:linear-gradient(90deg,#2bb5cf 0%,#3cc0d8 50%,#7fd4e3 100%);border-radius:0 0 120px 0}
.cta-photo{left:640px;top:0;width:560px;height:365px;background:linear-gradient(90deg,rgba(255,255,255,0),rgba(236,246,249,.85) 45%,#e8f3f6)}
.cta-title{left:160px;top:70px;font-family:"Raleway",sans-serif}
.cta-title .l1{font-size:32px;line-height:1.3;color:#fff}
.cta-title .l2{font-size:40px;font-weight:800;color:#fff;line-height:1.2}
.cta-btn{left:160px;top:275px;display:flex;gap:16px;align-items:center}
.btn-ghost{border:2px solid #fff;color:#fff;padding:9px 24px}

/* affiliates */
.affiliates{top:4545px;height:120px}
.affiliates h3{position:absolute;left:0;top:16px;width:1200px;text-align:center;font-size:13px;font-weight:700;letter-spacing:2px;color:var(--muted)}
.aff-row{position:absolute;left:150px;top:52px;width:900px;display:flex;justify-content:space-between}
.aff-row i{display:block;width:130px;height:48px;border-radius:24px;background:var(--soft);box-shadow:0 4px 12px rgba(20,40,60,.08)}

/* footer */
.footer{top:4665px;height:290px;background:var(--night);border-radius:60px 0 0 0}
.fcol{top:45px;color:#c9ccd0;font-size:12px}
.fcol h4{color:#fff;font-size:16px;font-weight:700;letter-spacing:1px;margin-bottom:16px}
.fcol b{color:#fff;font-size:12px;display:block;margin-top:6px}
.fcol ul{list-style:none;line-height:2}
.form{display:grid;grid-template-columns:1fr 1fr;gap:14px 24px;width:360px}
.field{border-bottom:1px solid #6b6f74;color:#c9ccd0;font-size:12px;padding-bottom:4px}
.field.wide{grid-column:1/3;height:44px}
.submit{border:1px solid #fff;color:#fff;font-size:12px;padding:4px 22px;width:max-content;margin-top:6px;border-radius:16px}
.bottom{top:4955px;height:87px;background:var(--night-2)}
.bottom p{position:absolute;left:75px;top:32px;font-size:11.5px;color:#9ea3a8}
.social{position:absolute;right:75px;top:30px;display:flex;gap:8px}
.social i{width:24px;height:24px;border-radius:50%;display:block}
</style>
</head>
<body>

<header class="section hero">
  <div class="abs hero-photo" role="img" aria-label="Photo of a woman holding her sore ankle, legs in pale pink skin tones"></div>
  <div class="abs brand"><i></i>Calderwyn Health</div>
  <div class="abs topbar">
    <span><svg viewBox="0 0 24 24" fill="none" stroke="#2bb5cf" stroke-width="2"><path d="M5 3h4l2 5-3 2a12 12 0 0 0 6 6l2-3 5 2v4a2 2 0 0 1-2 2A18 18 0 0 1 3 5a2 2 0 0 1 2-2z"/></svg>(08) 5550 1842</span>
    <span><svg viewBox="0 0 24 24" fill="none" stroke="#2bb5cf" stroke-width="2"><rect x="3" y="5" width="18" height="16" rx="1"/><path d="M3 10h18M8 3v4M16 3v4"/></svg>BOOK AN APPOINTMENT</span>
  </div>
  <nav class="abs nav">
    <span>Common Problems</span><span>Services</span><span>About Us</span><span>Case Histories</span><span>Helpful Information</span><span>Blog</span><span>Contact</span>
    <svg viewBox="0 0 24 24" fill="none" stroke="#262a2e" stroke-width="2.5"><circle cx="10" cy="10" r="7"/><path d="M15 15l6 6"/></svg>
  </nav>
  <div class="abs hero-title">
    <div class="l1">We Offer <span class="teal">Solutions</span> To Common</div>
    <div class="l2">FOOT PROBLEMS</div>
  </div>
  <p class="abs hero-text">When you suffer from a foot and/or ankle problem, the pain and discomfort can make it a challenge to engage in simple, daily activities. When the pain disrupts your life you need to contact a skilled, experienced podiatrist to get resolution.</p>
  <div class="abs hero-cta">
    <svg class="arrow" viewBox="0 0 34 12"><path d="M34 6H3M8 1L2 6l6 5" fill="none" stroke="#2bb5cf" stroke-width="2"/></svg>
    <span class="btn btn-solid" style="text-transform:none">Find It More</span>
  </div>
</header>

<section class="section pain">
  <div class="abs pain-box"></div>
  <div class="abs pain-title">
    <div class="l1">Let us <span class="teal">relive you</span> from</div>
    <div class="l2">YOUR PAIN</div>
  </div>
  <p class="abs pain-text">Our clinic has provided comprehensive podiatry care to all age groups across Western Australia since 1991. Since our practice was established, our success has allowed us to grow and expand our services, currently hosting six on-staff foot podiatrists, and a variety of the most advanced techniques and equipment to treat foot and ankle pain. In our Marrowby office, we can advise you on many matters relating to your feet and legs, including footwear, skin care, walking difficulties, and sports injuries.</p>
  <div class="abs readmore">Read More <svg class="arrow" viewBox="0 0 34 12"><path d="M0 6h31M26 1l6 5-6 5" fill="none" stroke="#2bb5cf" stroke-width="2"/></svg></div>
  <div class="abs pain-photo" role="img" aria-label="Photo of a seated man in white shorts holding his foot, wearing red sneakers"></div>
</section>

<section class="section practice">
  <div class="abs sec-head" style="top:65px"><h2>OUR PRACTICE AREAS</h2><p>Lorem ipsum is simply dummy text</p></div>
  <div class="abs practice-card">
    <div class="abs practice-photo" role="img" aria-label="Photo of a runner on a forest trail clutching an injured ankle"><span>ANKLE INJURIES</span></div>
    <div class="abs tabs"><div class="on">Common Problems</div><div>Foot &amp; Ankle Surgery</div><div>Sport and Dance</div><div>All Our Services</div></div>
    <p class="abs practice-text">When you suffer from a foot and/or ankle problem, the pain and discomfort can make it a challenge to engage in simple daily activities. When the pain disrupts your life you need to contact a skilled, experienced podiatrist to get resolution. The podiatrists at Calderwyn Health offer a variety of treatment options for many common foot and ankle conditions, including Achilles tendon injuries, ankle sprains, flat foot and cavus foot, and bunions and ingrown toenails. Their primary concern is the health of their patients' feet and ankles, and they use advanced equipment and work with other professionals, including trainers and physical therapists, to ensure a successful outcome. To discuss your foot and ankle pain, contact our Marrowby office at (08) 5550 1842.</p>
    <div class="abs cond">
      <span>Achilles Tendon Injuries</span><span>Corns and Callouses</span><span>Ingrown Toenails</span>
      <span>Ankle Sprains</span><span>Heel and Arch Pain</span><span>Fungal Nails</span>
      <span>Bunions</span><span>High Arch Feet (Pes Cavus)</span><span>Flatfeet</span>
      <span>Skin and Nail Care</span><span>Stiff Big Toe (Hallux Rigidus)</span><span class="more">View More</span>
    </div>
  </div>
</section>

<section class="section walks">
  <div class="abs band"></div>
  <div class="abs doctor" role="img" aria-label="Photo of a smiling female doctor in a white coat with a stethoscope"></div>
  <div class="abs walks-title"><div class="l1">Caring for Patients From All</div><div class="l2">WALKS OF LIFE</div></div>
  <p class="abs walks-text">We know it can be difficult to seek treatment for a condition, especially if the only forward could mean surgery or a lengthy recovery. That is why we use every advantage to ease our customers' minds as well as their discomfort. In our offices, we help our patients:</p>
  <div class="abs band-item" style="top:330px"><svg viewBox="0 0 24 24" fill="none" stroke="#fff" stroke-width="2.5"><path d="M9 5l7 7-7 7"/></svg>REGAIN CONTROL</div>
  <p class="abs band-text">Just like you, we want you to get better as soon as possible. That is why we focus on making your visit an informative and supportive experience, empowering you to take control of your condition and make the best possible treatment choice. We even offer specific solutions to athletes, such as ballet dancers, football players, and others suffering from sporting injuries.</p>
  <div class="abs band-item" style="top:475px"><svg viewBox="0 0 24 24" fill="none" stroke="#fff" stroke-width="2.5"><path d="M9 5l7 7-7 7"/></svg>EXPLORE ALL POSSIBLE SOLUTIONS</div>
  <div class="abs band-item" style="top:540px"><svg viewBox="0 0 24 24" fill="none" stroke="#fff" stroke-width="2.5"><path d="M9 5l7 7-7 7"/></svg>STAY PAIN-FREE FOR LIFE</div>
  <div class="abs walks-cta">
    <span class="btn btn-line">Contact Us Today</span>
    <svg class="arrow" viewBox="0 0 34 12"><path d="M0 6h31M26 1l6 5-6 5" fill="none" stroke="#2bb5cf" stroke-width="2"/></svg>
  </div>
</section>

<section class="section team">
  <div class="abs team-title"><div class="l1">Meet Our Team of</div><div class="l2">EXPERTS</div></div>
  <p class="abs team-text">We combine our state-of-the-art equipment and medical experience with our competent, friendly staff, making it as easy as possible for our patients to get relief. It is our goal for you to walk away with your problems.</p>
  <svg class="abs team-grid" viewBox="0 0 1200 690">
    <g fill="#fff" stroke="#e5e7ea" stroke-width="1.5" stroke-linejoin="round">
      <polygon points="974,115 1120,261 974,407 828,261"/>
      <polygon points="218,195 355,332 218,469 81,332"/>
      <polygon points="487,175 645,333 487,491 329,333"/>
      <polygon points="823,215 960,352 823,489 686,352"/>
      <polygon points="319,362 456,499 319,636 182,499"/>
      <polygon points="672,362 809,499 672,636 535,499"/>
    </g>
    <g role="img" aria-label="Portrait photos of the podiatry team members" stroke-linejoin="round" stroke-width="10">
      <polygon points="974,140 1095,261 974,382 853,261" fill="#e7d5c4" stroke="#e7d5c4"/>
      <polygon points="218,220 330,332 218,444 106,332" fill="#d9c4b2" stroke="#d9c4b2"/>
      <polygon points="487,200 620,333 487,466 354,333" fill="#dcc2ad" stroke="#dcc2ad"/>
      <polygon points="823,240 935,352 823,464 711,352" fill="#e3cfbd" stroke="#e3cfbd"/>
      <polygon points="319,387 431,499 319,611 207,499" fill="#cdb6a5" stroke="#cdb6a5"/>
      <polygon points="672,387 784,499 672,611 560,499" fill="#e0cbb8" stroke="#e0cbb8"/>
    </g>
    <rect x="420" y="355" width="134" height="36" rx="18" fill="#2bb5cf"/>
    <text x="487" y="371" text-anchor="middle" font-family="Raleway,sans-serif" font-size="11" font-weight="700" fill="#fff">Dr Owen Farrel</text>
    <text x="487" y="385" text-anchor="middle" font-family="Open Sans,sans-serif" font-size="9" fill="#eafaff">Podiatrist</text>
  </svg>
</section>

<section class="section offer">
  <div class="abs offer-title"><div class="l1">Get Your Foot Surgery Book</div><div class="l2">FOR FREE</div><div class="by">Podiatric Surgeon Dr Ellis Marr</div></div>
  <div class="abs book">
    <h4>Podiatric Surgery</h4>
    <p>Dr Ellis Marr<br>Calderwyn Health<br>Clear answers on foot<br>surgery for patients<br>and their families</p>
    <div class="pic" role="img" aria-label="Photo of surgeons in scrubs at work in an operating theatre"></div>
  </div>
  <p class="abs book-caption">This book was created to demonstrate examples of some foot conditions that can be surgically corrected by our Podiatric Surgeon</p>
  <div class="abs divider"></div>
  <div class="abs cases-title"><div class="l1">Problems we have solved &amp; their</div><div class="l2">CASE HISTORIES</div></div>
  <div class="abs cases">
    <div class="case">Plantar fascia Case<svg viewBox="0 0 24 24" fill="none" stroke="#2bb5cf" stroke-width="1.6"><circle cx="12" cy="12" r="10"/><path d="M12 7v10M7 12h10"/></svg></div>
    <div class="case">Bunion Case<svg viewBox="0 0 24 24" fill="none" stroke="#2bb5cf" stroke-width="1.6"><circle cx="12" cy="12" r="10"/><path d="M12 7v10M7 12h10"/></svg></div>
    <div class="case">Trauma Case<svg viewBox="0 0 24 24" fill="none" stroke="#2bb5cf" stroke-width="1.6"><circle cx="12" cy="12" r="10"/><path d="M12 7v10M7 12h10"/></svg></div>
    <div class="case">Plantar fascia Case<svg viewBox="0 0 24 24" fill="none" stroke="#2bb5cf" stroke-width="1.6"><circle cx="12" cy="12" r="10"/><path d="M12 7v10M7 12h10"/></svg></div>
    <div class="case">Bunion Case<svg viewBox="0 0 24 24" fill="none" stroke="#2bb5cf" stroke-width="1.6"><circle cx="12" cy="12" r="10"/><path d="M12 7v10M7 12h10"/></svg></div>
    <div class="case">Trauma Case<svg viewBox="0 0 24 24" fill="none" stroke="#2bb5cf" stroke-width="1.6"><circle cx="12" cy="12" r="10"/><path d="M12 7v10M7 12h10"/></svg></div>
    <div class="case">Plantar fascia Case<svg viewBox="0 0 24 24" fill="none" stroke="#2bb5cf" stroke-width="1.6"><circle cx="12" cy="12" r="10"/><path d="M12 7v10M7 12h10"/></svg></div>
    <div class="case">Bunion Case<svg viewBox="0 0 24 24" fill="none" stroke="#2bb5cf" stroke-width="1.6"><circle cx="12" cy="12" r="10"/><path d="M12 7v10M7 12h10"/></svg></div>
  </div>
</section>

<div class="section strip">It doesn't take long before a foot injury may cause wide-ranging consequences</div>
<section class="section cta">
  <div class="abs cta-photo" role="img" aria-label="Photo of a clinician wrapping a patient's foot in a bandage"></div>
  <div class="abs cta-title"><div class="l1">We are Here to help you book an<br>appointment and Relive yourself</div><div class="l2">FROM PAIN</div></div>
  <div class="abs cta-btn">
    <span class="btn btn-ghost">Book an Appointment Today</span>
    <svg class="arrow" viewBox="0 0 34 12"><path d="M0 6h31M26 1l6 5-6 5" fill="none" stroke="#fff" stroke-width="2"/></svg>
  </div>
</section>

<section class="section affiliates">
  <h3>OUR TRUSTED AFFILIATES</h3>
  <div class="aff-row" role="img" aria-label="Badges of affiliated health organisations">
    <i></i><i></i><i></i><i></i><i></i><i></i>
  </div>
</section>

<footer class="section footer">
  <div class="abs fcol" style="left:75px">
    <h4>CONTACT INFO</h4>
    <b>Address</b>Marrowby Office: 12 Crestmoor Road, Marrowby<br>WA 6154
    <b style="margin-top:14px">Phone</b>+61 (08) 5550 1842
    <b style="margin-top:14px">E-Mail</b>hello@calderwynhealth.com.au
  </div>
  <div class="abs fcol" style="left:430px">
    <h4>QUICK LINKS</h4>
    <ul><li>Bunion Surgery</li><li>Hammer Toes and Mallet Toes</li><li>Ingrown Toenail Surgery</li><li>Morton's Neuroma</li><li>Lateral Ankle Repair</li><li>Ballet Shoes &amp; Pointe Shoes</li><li>Laser Therapy for Sports Injuries</li><li>Sports Rehabilitation</li></ul>
  </div>
  <div class="abs fcol" style="left:770px">
    <h4>GET IN TOUCH</h4>
    <div class="form">
      <div class="field">First Name</div><div class="field">Last Name</div>
      <div class="field">Phone Number</div><div class="field">E-mail</div>
      <div class="field wide">Message</div>
      <div class="submit">Submit</div>
    </div>
  </div>
</footer>
<div class="section bottom">
  <p>©2017 Calderwyn Health. All Rights Reserved. Reproduced with Permission. Privacy Policy</p>
  <div class="social"><i style="background:#3b5998"></i><i style="background:#2bb5cf"></i><i style="background:#dd4b39"></i><i style="background:#1f7fb8"></i></div>
</div>

</body>
</html>
```